Brochure for Varesh Law firm

We would like to have a brochure that describes the Firm ( about the firm) , the vision, the team , the practice areas. And the contact.
Varesh law firm has ranked as top Libyan law firms by Juris Ledger.
It will give a good picture if you look at www.varesh-example.ly

We can also provide more information if requested to share with designer.

```html
<!DOCTYPE html>
<html lang="en">
<head>
<meta charset="utf-8">
<title>Varesh Law Firm Brochure</title>
<link href="https://fonts.googleapis.com/css2?family=Montserrat:wght@300;400;500;700;800&display=swap" rel="stylesheet">
<style>
:root{
  --bg:#d3d3d3;
  --blue:#2347b8;
  --blue-deep:#1d3ca6;
  --blue-soft:#3a63d4;
  --blue-accent:#5b8cf5;
  --ink:#1b1b24;
  --paper:#ffffff;
  --paper-shade:#f1f1f3;
  --white:#ffffff;
}
*{box-sizing:border-box;margin:0;padding:0}
html,body{width:1200px;height:2400px;overflow:hidden}
body{background:var(--bg);font-family:"Montserrat",Arial,sans-serif;color:var(--ink);position:relative}
.page{position:absolute;background:var(--paper);overflow:hidden;box-shadow:0 6px 18px rgba(0,0,0,.18)}
.brand-name{font-family:"Montserrat",Arial,sans-serif;font-weight:500;letter-spacing:.5px;color:var(--ink)}
.brand-name.light{color:var(--white)}

/* front cover */
.front-cover{left:370px;top:60px;width:460px;height:650px}
.cover-photo{position:absolute;inset:0;background:
  linear-gradient(180deg,#f6eef0 0%,#ead9dc 22%,#b9b6bd 45%,#8f9aa6 62%,#6f7f8e 80%,#5d6c7a 100%)}
.cover-photo .warm{position:absolute;left:24%;top:30%;width:56%;height:28%;border-radius:40%;background:radial-gradient(ellipse,#d9a993 0%,rgba(217,169,147,0) 70%)}
.front-cover .brand-name,.spread-front .brand-name{position:absolute;right:34px;top:44px;font-size:34px}
.cover-band{position:absolute;left:0;bottom:0;width:100%;height:100%}
.cover-text{position:absolute;right:30px;bottom:48px;text-align:right;color:var(--white)}
.cover-text .firm{font-size:19px;font-weight:400}
.cover-text .headline{font-size:23px;font-weight:800;margin-top:4px}
.cover-text .headline span{color:var(--blue-accent)}
.cover-text .motto{font-size:14px;font-weight:400;margin-top:4px;padding-bottom:8px;border-bottom:1.5px solid var(--white)}
.cover-text .web{font-size:14px;letter-spacing:4px;margin-top:12px;text-align:center}

/* spread */
.spread{left:120px;width:960px;height:680px}
.spread-outer{top:790px}
.spread-inner{top:1590px;background:linear-gradient(90deg,var(--paper) 0%,var(--paper) 47%,var(--paper-shade) 50%,var(--paper) 53%,var(--paper) 100%)}
.half{position:absolute;top:0;width:480px;height:680px;overflow:hidden}
.half.left{left:0}.half.right{left:480px}
.spread-outer .cover-text{right:28px;bottom:40px}
.back-photo{position:absolute;inset:0;background:
  linear-gradient(180deg,#ffffff 0%,#eef0f3 18%,#cfc4c6 36%,#9d8c8f 50%,#8a98a4 62%,#c9d1d8 78%,#e6eaee 100%)}
.back-contacts{position:absolute;left:0;bottom:0;width:100%;height:170px;display:flex;align-items:center;padding:0 24px;color:var(--white)}
.back-contacts .brand-name{font-size:30px;padding-right:20px;border-right:1.5px solid var(--white);margin-right:18px}
.office{font-size:9.5px;line-height:1.5;margin-right:20px}
.office h3{font-size:11px;font-weight:700;padding-bottom:3px;margin-bottom:4px;border-bottom:1px solid var(--white);display:inline-block}
.office p{display:flex;gap:5px;align-items:flex-start}
.office svg{flex:none;margin-top:2px}

/* services */
.services-head{position:absolute;left:44px;top:70px;padding-left:12px;border-left:5px solid var(--blue)}
.services-head h2{font-size:30px;font-weight:800;line-height:1}
.services-head p{font-size:12px;margin-top:8px;line-height:1.35;max-width:360px}
.tile{position:absolute;width:188px;height:156px;background:linear-gradient(135deg,var(--blue-deep),var(--blue-soft));color:var(--white);text-align:center;padding:20px 12px 0}
.tile svg{display:block;margin:0 auto 8px}
.tile h4{font-size:17px;font-weight:400;line-height:1.1}
.tile p{font-size:9px;margin-top:5px;line-height:1.3}
.page-foot{position:absolute;bottom:30px;display:flex;align-items:center;gap:10px;font-size:10px;font-weight:700}
.page-foot i{display:block;height:1px;width:280px;background:var(--ink)}
.spread-inner .brand-name{position:absolute;right:40px;top:40px;font-size:30px}
</style>
</head>
<body>

<!-- front cover -->
<section class="page front-cover">
  <div class="cover-photo" role="img" aria-label="Photo of a business handshake over a city skyline"><div class="warm"></div></div>
  <svg class="cover-band" viewBox="0 0 460 650" preserveAspectRatio="none">
    <polygon points="0,442 460,402 460,410 0,450" fill="#ffffff"/>
    <polygon points="0,452 460,412 460,650 0,650" fill="#2347b8"/>
  </svg>
  <span class="brand-name">Varesh</span>
  <div class="cover-text">
    <p class="firm">Varesh Law Firm</p>
    <p class="headline">Setting The Standard For <span>Libya</span></p>
    <p class="motto">Excellence is the hallmark of our legal solutions.</p>
    <p class="web">www.varesh-example.ly</p>
  </div>
</section>

<!-- back and front cover spread -->
<section class="page spread spread-outer">
  <div class="half left">
    <div class="back-photo" role="img" aria-label="Photo of a city skyline seen through office glass"></div>
    <svg class="cover-band" viewBox="0 0 480 680" preserveAspectRatio="none">
      <polygon points="0,500 480,470 480,478 0,508" fill="#ffffff"/>
      <polygon points="0,510 480,480 480,680 0,680" fill="#2347b8"/>
    </svg>
    <div class="back-contacts">
      <span class="brand-name light">Varesh</span>
      <div class="office">
        <h3>Tripoli Office</h3>
        <p><svg width="8" height="10" viewBox="0 0 8 10"><path d="M4 0a4 4 0 0 1 4 4c0 3-4 6-4 6S0 7 0 4a4 4 0 0 1 4-4z" fill="#fff"/></svg>12, Meridian Tower 3<br>P.O. Box 40210<br>Tripoli, Libya</p>
        <p><svg width="9" height="9" viewBox="0 0 9 9"><path d="M1 0l2 2-1 1.5a6 6 0 0 0 3.5 3.5L7 6l2 2-1 1C3 9 0 6 0 1z" fill="#fff"/></svg>+218 21 0000111</p>
        <p><svg width="8" height="8" viewBox="0 0 8 8"><circle cx="4" cy="4" r="4" fill="#fff"/></svg>www.varesh-example.ly</p>
      </div>
      <div class="office">
        <h3>Benghazi Office</h3>
        <p><svg width="8" height="10" viewBox="0 0 8 10"><path d="M4 0a4 4 0 0 1 4 4c0 3-4 6-4 6S0 7 0 4a4 4 0 0 1 4-4z" fill="#fff"/></svg>Shari' Al Nakheel, Sidi Hamad,<br>Eastern Quarter<br>Benghazi, Libya</p>
        <p><svg width="9" height="9" viewBox="0 0 9 9"><path d="M1 0l2 2-1 1.5a6 6 0 0 0 3.5 3.5L7 6l2 2-1 1C3 9 0 6 0 1z" fill="#fff"/></svg>+218 92 000 2244</p>
        <p><svg width="8" height="8" viewBox="0 0 8 8"><circle cx="4" cy="4" r="4" fill="#fff"/></svg>www.varesh-example.ly</p>
      </div>
    </div>
  </div>
  <div class="half right spread-front">
    <div class="cover-photo" role="img" aria-label="Photo of a business handshake over a city skyline"><div class="warm"></div></div>
    <svg class="cover-band" viewBox="0 0 480 680" preserveAspectRatio="none">
      <polygon points="0,500 480,470 480,478 0,508" fill="#ffffff"/>
      <polygon points="0,510 480,480 480,680 0,680" fill="#2347b8"/>
    </svg>
    <span class="brand-name">Varesh</span>
    <div class="cover-text">
      <p class="firm">Varesh Law Firm</p>
      <p class="headline">Setting The Standard For <span>Libya</span></p>
      <p class="motto">Excellence is the hallmark of our legal solutions.</p>
      <p class="web">www.varesh-example.ly</p>
    </div>
  </div>
</section>

<!-- inner services spread -->
<section class="page spread spread-inner">
  <div class="half left">
    <div class="services-head">
      <h2>Varesh Law Services</h2>
      <p>In addition to legal solutions that we provide our clients, our services in Libya include the following practises:</p>
    </div>
    <div class="tile" style="left:40px;top:220px">
      <svg width="40" height="40" viewBox="0 0 40 40" fill="none" stroke="#fff" stroke-width="2"><circle cx="12" cy="10" r="5"/><circle cx="28" cy="10" r="5"/><path d="M4 26c0-6 16-6 16 0M20 26c0-6 16-6 16 0M2 30h36"/></svg>
      <h4>Consultation</h4><p>Varesh provides consultation legal practice in Libya</p>
    </div>
    <div class="tile" style="left:246px;top:180px">
      <svg width="40" height="40" viewBox="0 0 40 40" fill="none" stroke="#fff" stroke-width="2"><rect x="8" y="8" width="16" height="8" transform="rotate(-30 16 12)"/><path d="M20 18l12 14M6 34h16"/></svg>
      <h4>Litigation</h4><p>Varesh provides Litigation practice in Libya</p>
    </div>
    <div class="tile" style="left:40px;top:394px">
      <svg width="40" height="40" viewBox="0 0 40 40" fill="none" stroke="#fff" stroke-width="2"><path d="M20 4v30M8 10h24M8 10l-5 12h10zM32 10l-5 12h10zM12 34h16"/></svg>
      <h4>Arbitration</h4><p>Varesh provides arbitration legal practice in Libya</p>
    </div>
    <div class="tile" style="left:246px;top:354px">
      <svg width="40" height="40" viewBox="0 0 40 40" fill="none" stroke="#fff" stroke-width="2"><rect x="5" y="7" width="30" height="24" rx="2"/><path d="M5 13h30M10 19h10M10 24h14"/></svg>
      <h4>Commercial Registration</h4><p>Varesh provides commercial registration services in Libya</p>
    </div>
    <div class="page-foot" style="left:44px"><span>www.varesh-example.ly</span><i></i></div>
  </div>
  <div class="half right">
    <span class="brand-name">Varesh</span>
    <div class="tile" style="left:50px;top:180px">
      <svg width="40" height="40" viewBox="0 0 40 40" fill="none" stroke="#fff" stroke-width="2"><path d="M20 4l13 5v10c0 8-6 13-13 16-7-3-13-8-13-16V9z"/><path d="M14 20l4 4 8-8"/></svg>
      <h4>Investment Licence</h4><p>Varesh provides investment licence services in Libya</p>
    </div>
    <div class="tile" style="left:256px;top:140px">
      <svg width="40" height="40" viewBox="0 0 40 40" fill="none" stroke="#fff" stroke-width="2"><rect x="9" y="6" width="22" height="28" rx="2"/><path d="M15 6V3h10v3M14 15l2 2 4-4M14 25l2 2 4-4M23 15h4M23 25h4"/></svg>
      <h4>Legal Risk Assessment</h4><p>Varesh provides legal risk assessment services in Libya</p>
    </div>
    <div class="tile" style="left:50px;top:354px">
      <svg width="40" height="40" viewBox="0 0 40 40" fill="none" stroke="#fff" stroke-width="2"><rect x="7" y="5" width="20" height="26" rx="2"/><path d="M12 12h10M12 18h10M12 24h6"/><circle cx="27" cy="27" r="6"/><path d="M31 31l5 5"/></svg>
      <h4>Due-Diligence</h4><p>Varesh provides due-diligence services in Libya</p>
    </div>
    <div class="tile" style="left:256px;top:314px">
      <svg width="40" height="40" viewBox="0 0 40 40" fill="none" stroke="#fff" stroke-width="2"><circle cx="20" cy="16" r="9"/><path d="M16 25v5h8v-5M17 34h6"/></svg>
      <h4>Intellectual Property</h4><p>Varesh provides intellectual property services in Libya</p>
    </div>
    <div class="page-foot" style="right:40px"><i></i><span>www.varesh-example.ly</span></div>
  </div>
</section>

</body>
</html>
```